Create banners that convert into clicks

I'm looking for a for a banner that with following details.
top slogan:
We Make Your Phone Ring.

ROI Driven SEO & PPC Campaigns.
No Hype! Just Results!

Bottom: Get A Free SEO & PPC Analysis

Image: Picture of phone off hook.
Logos and Colors Attached

Banner Sizes needed:
728x90
300x250
480x60
Updates

Reason: Not changes by designers per messages sent. would like at least 2 days.

Target Market(s)

Small To Med Size business owners

Industry/Entity Type

Seo

Requirements
Must have
• Please keep to main color scheme of logo...Blue & White.
May use a bright color to draw attention like yellow or orange or similar.

```html
<!DOCTYPE html>
<html lang="en">
<head>
<meta charset="utf-8">
<title>Brightline Marketing – Banner Set</title>
<link rel="stylesheet" href="https://fonts.googleapis.com/css2?family=Open+Sans:wght@400;600;700&display=swap">
<style>
  :root {
    --canvas-bg: #ece7df;
    --banner-blue: #1b6fd8;
    --logo-white: #ffffff;
    --logo-navy: #1b3c78;
    --text-white: #ffffff;
    --text-soft-blue: #cfe2ff;
    --cta-top: #f9a01c;
    --cta-bottom: #e2740a;
    --device-light: #c9ccd1;
    --device-dark: #3a3d42;
  }
  * { box-sizing: border-box; margin: 0; padding: 0; }
  html, body { width: 1200px; height: 818px; overflow: hidden; }
  body {
    position: relative;
    background: var(--canvas-bg);
    font-family: "Open Sans", Arial, sans-serif;
  }
  .banner {
    position: absolute;
    background: var(--banner-blue);
    overflow: hidden;
    box-shadow: 3px 4px 8px rgba(0,0,0,0.35);
  }
  .banner-logo-plate { position: absolute; left: 0; top: 0; }
  .brand-name {
    position: absolute;
    color: var(--logo-navy);
    font-weight: 600;
    letter-spacing: 0.02em;
    white-space: nowrap;
    text-transform: uppercase;
  }
  .headline {
    position: absolute;
    color: var(--text-white);
    font-weight: 400;
    white-space: nowrap;
    line-height: 1.1;
  }
  .headline strong { font-weight: 700; }
  .subline {
    position: absolute;
    color: var(--text-soft-blue);
    font-weight: 700;
    white-space: nowrap;
    line-height: 1.2;
  }
  .cta {
    position: absolute;
    display: flex;
    align-items: center;
    justify-content: center;
    background: linear-gradient(var(--cta-top), var(--cta-bottom));
    color: var(--text-white);
    font-weight: 700;
    white-space: nowrap;
  }
  .device-art {
    position: absolute;
    border-radius: 10px;
    background: linear-gradient(135deg, var(--device-light), #8d9299 40%, var(--device-dark) 60%, var(--device-light));
  }

  /* 728 x 90 leaderboard */
  .banner--leaderboard { left: 152px; top: 106px; width: 897px; height: 111px; }
  .banner--leaderboard .brand-name { left: 12px; top: 14px; font-size: 17px; }
  .banner--leaderboard .headline { left: 472px; top: 12px; transform: translateX(-50%); font-size: 27px; }
  .banner--leaderboard .subline { left: 472px; top: 46px; transform: translateX(-50%); font-size: 16px; }
  .banner--leaderboard .cta { left: 329px; top: 76px; width: 275px; height: 32px; font-size: 14px; }
  .banner--leaderboard .device-art { left: 718px; top: 10px; width: 132px; height: 80px; transform: rotate(9deg); }

  /* 468 x 60 banner */
  .banner--full { left: 312px; top: 248px; width: 577px; height: 74px; }
  .banner--full .brand-name { left: 8px; top: 9px; font-size: 12px; }
  .banner--full .headline { left: 292px; top: 5px; transform: translateX(-50%); font-size: 18px; }
  .banner--full .subline { left: 292px; top: 27px; transform: translateX(-50%); font-size: 12px; }
  .banner--full .cta { left: 182px; top: 48px; width: 222px; height: 25px; font-size: 11px; }
  .banner--full .device-art { left: 462px; top: 9px; width: 88px; height: 54px; border-radius: 7px; transform: rotate(9deg); }

  /* 300 x 250 medium rectangle */
  .banner--rectangle { left: 415px; top: 376px; width: 370px; height: 308px; }
  .banner--rectangle .brand-name { left: 22px; top: 20px; font-size: 18px; }
  .banner--rectangle .headline { left: 32px; top: 90px; font-size: 27px; line-height: 1.18; }
  .banner--rectangle .subline { left: 121px; top: 172px; transform: translateX(-50%); font-size: 16px; text-align: center; }
  .banner--rectangle .cta { left: 12px; top: 253px; width: 342px; height: 40px; font-size: 17px; }
  .banner--rectangle .device-art { left: 246px; top: 44px; width: 102px; height: 172px; border-radius: 12px; transform: rotate(4deg); }
</style>
</head>
<body>

  <section class="banner banner--leaderboard" aria-label="728 by 90 banner">
    <svg class="banner-logo-plate" width="260" height="54" viewBox="0 0 260 54"><polygon points="0,0 255,0 203,52 0,52" fill="var(--logo-white)"/></svg>
    <span class="brand-name">Brightline Marketing</span>
    <h2 class="headline">We Make Your Phone <strong>Ring</strong></h2>
    <p class="subline">ROI Driven SEO &amp; PPC Campaigns.</p>
    <a class="cta">Get A Free SEO &amp; PPC Analysis</a>
    <div class="device-art" role="img" aria-label="Smartphone lying on its side showing an incoming call icon"></div>
  </section>

  <section class="banner banner--full" aria-label="468 by 60 banner">
    <svg class="banner-logo-plate" width="165" height="35" viewBox="0 0 165 35"><polygon points="0,0 160,0 132,33 0,33" fill="var(--logo-white)"/></svg>
    <span class="brand-name">Brightline Marketing</span>
    <h2 class="headline">We Make Your Phone <strong>Ring</strong></h2>
    <p class="subline">ROI Driven SEO &amp; PPC Campaigns.</p>
    <a class="cta">Get A Free SEO &amp; PPC Analysis</a>
    <div class="device-art" role="img" aria-label="Smartphone lying on its side showing an incoming call icon"></div>
  </section>

  <section class="banner banner--rectangle" aria-label="300 by 250 banner">
    <svg class="banner-logo-plate" width="285" height="60" viewBox="0 0 285 60"><polygon points="0,0 281,0 222,59 0,59" fill="var(--logo-white)"/></svg>
    <span class="brand-name">Brightline Marketing</span>
    <h2 class="headline">We Make Your<br>Phone <strong>Ring</strong></h2>
    <p class="subline">ROI Driven SEO<br>&amp; PPC Campaigns.</p>
    <a class="cta">Get A Free SEO &amp; PPC Analysis</a>
    <div class="device-art" role="img" aria-label="Upright smartphone showing an incoming call icon"></div>
  </section>

</body>
</html>
```